Visitenkarten-Design für Immobilien-Unternehmen
Designer ist sehr bemüht und die Änderungswünsche wurden rasch bearbeitet. Auch wurde im Nachhinein noch mein Wunsch auf Adaptierung zu einem Lackdruck bearbeitet und gesendet. Ich bin mit der Abwicklung vollkommen zufrieden - Vielen Dank
Zielgruppe
Die TOLU Immobilien GmbH ist eine durch Ing. Kilian Frühwald inhabergeführte Gesellschaft, welche sich schwerpunktmäßig mit Immobilieninvestitionen sowie Beteiligungen im Bereich von Wohn- und Gewerbeimmobilien beschäftigt. Das Unternehmen kauft, hält, vermietet und verkauft Liegenschaften aller Art, mit dem Fokus auf Gewerbe- und Wohnimmobilien. Zielgruppe sind Personen, welche Immobilien verkaufen möchten - wir betreiben nur eigene Vermögensverwaltung
siehe: www.tolu-immobilien.at
Aufgabenstellung
schlicht und einfach gehalten - weniger ist mehr - nur die wichtigsten Informationen auf der Visitenkarte.
siehe Homepage: www.tolu-immobilien.at

```html
<!DOCTYPE html>
<html lang="de">
<head>
<meta charset="utf-8">
<title>TOLU Immobilien GmbH – Visitenkarte</title>
<link rel="stylesheet" href="https://fonts.googleapis.com/css2?family=Raleway:wght@400&display=swap">
<style>
  :root {
    --backdrop: #353131;
    --card-light: #fbfbfa;
    --card-dark: #1e1d1d;
    --ink-dark: #3a3a3a;
    --ink-light: #f2f2f2;
  }
  html, body {
    margin: 0;
    padding: 0;
    overflow: hidden;
  }
  .canvas {
    width: 1200px;
    height: 900px;
    background: var(--backdrop);
    display: flex;
    align-items: center;
    justify-content: center;
    gap: 60px;
    font-family: "Raleway", sans-serif;
  }
  .card {
    position: relative;
    width: 510px;
    height: 330px;
    box-sizing: border-box;
    box-shadow: 0 10px 30px rgba(0, 0, 0, 0.35);
  }
  .card--front {
    background: var(--card-light);
    display: flex;
    align-items: center;
    justify-content: center;
  }
  .company-name {
    margin: 0;
    color: var(--ink-dark);
    font-weight: 400;
    font-size: 26px;
    letter-spacing: 0.12em;
    text-align: center;
    line-height: 1.35;
  }
  .card--back {
    background: var(--card-dark);
  }
  .contact {
    position: absolute;
    left: 44px;
    bottom: 46px;
    margin: 0;
    color: var(--ink-light);
    font-size: 17px;
    font-weight: 400;
    line-height: 1.3;
    letter-spacing: 0.02em;
    font-style: normal;
  }
</style>
</head>
<body>
  <main class="canvas">
    <section class="card card--front" aria-label="Vorderseite">
      <p class="company-name">TOLU<br>Immobilien GmbH</p>
    </section>
    <section class="card card--back" aria-label="Rückseite">
      <address class="contact">
        office@tolu-immobilien.at<br>
        +43 664 480 27 15
      </address>
    </section>
  </main>
</body>
</html>
```